Make it POP! Label design for Australian Skin Care range

I want to see elegance, femininity, luxury, glamour.
Design needs to compliment existing logo in style and colours; turquoise and silver (see file). text required (see file)
There are 5 different products with different text - same design required.
Please see file attached for the containers the labels will be applied to.

Target Market(s)

women over 35

Industry/Entity Type

Skin Care Product

Font styles to use
Sans Serif

Colors
33b8a4

Requirements
Must have
• Design in Turquoise and silver
• Sans Serif fonts, compliment existing logo (see file)
• contain text exactly as written (see file)
Nice to have
• Feminine, flowing lines/ shapes
Should not have
• Black, nothing bold or masculine. Nothing that looks clinical or medical

```html
<!DOCTYPE html>
<html lang="en">
<head>
<meta charset="utf-8">
<title>Lora's Grove – Native Hydrating Serum Label</title>
<link rel="stylesheet" href="https://fonts.googleapis.com/css2?family=Montserrat:wght@500;600;700&display=swap">
<style>
  :root {
    --turquoise: #33b8b4;
    --turquoise-soft: #6fd0cb;
    --ink: #4a4a4c;
    --paper: #ffffff;
    --backdrop: #efeff0;
  }
  * { box-sizing: border-box; margin: 0; padding: 0; }
  html, body {
    width: 1200px; height: 1200px; overflow: hidden;
    background: var(--backdrop);
  }
  .sheet { position: relative; width: 1200px; height: 1200px; }
  .label {
    position: absolute; top: 230px;
    width: 340px; height: 740px;
    background: var(--paper);
    overflow: hidden;
  }
  .label--front { left: 230px; }
  .label--back  { left: 630px; }
  .lace-pattern {
    position: absolute; inset: 0;
    background:
      radial-gradient(ellipse at 75% 20%, var(--turquoise) 0%, rgba(51,184,180,0) 55%),
      radial-gradient(ellipse at 20% 85%, var(--turquoise) 0%, rgba(51,184,180,0) 55%),
      linear-gradient(160deg, var(--turquoise-soft), #9fe0dc 50%, var(--turquoise-soft));
  }
  .panel {
    position: absolute; left: 25px; top: 132px;
    width: 290px; height: 425px;
    border-radius: 50%;
    background: var(--paper);
    border: 5px solid var(--turquoise);
    display: flex; flex-direction: column; align-items: center; justify-content: center;
    text-align: center;
    font-family: "Montserrat", sans-serif;
    color: var(--ink);
  }
  .brand-name {
    font-size: 14px; font-weight: 600; letter-spacing: 0.12em;
    color: var(--ink);
    margin-top: 30px; margin-bottom: 16px;
  }
  .tagline {
    font-size: 7.5px; font-weight: 600; letter-spacing: 0.24em; line-height: 1.6;
    margin-bottom: 16px;
  }
  .product-name {
    font-size: 15px; font-weight: 700; letter-spacing: 0.34em; line-height: 1.75;
    color: var(--turquoise); margin-bottom: 14px; padding-left: 0.34em;
  }
  .actives {
    font-size: 7px; font-weight: 600; letter-spacing: 0.22em; line-height: 1.6;
    margin-bottom: 12px;
  }
  .claims {
    font-size: 5.6px; font-weight: 600; letter-spacing: 0.2em; margin-bottom: 12px;
  }
  .volume { font-size: 7px; font-weight: 600; letter-spacing: 0.24em; }
  .panel--info { padding: 0 30px; }
  .info-block {
    font-size: 5.6px; font-weight: 600; letter-spacing: 0.16em; line-height: 1.95;
    text-transform: uppercase; margin-bottom: 9px;
  }
  .info-block:last-child { margin-bottom: 0; }
  .info-block--narrow { padding: 0 22px; }
</style>
</head>
<body>
<main class="sheet">

  <section class="label label--front">
    <div class="lace-pattern" role="img" aria-label="Turquoise floral lace pattern on a white honeycomb net"></div>
    <div class="panel">
      <p class="brand-name">LORA'S GROVE</p>
      <p class="tagline">NATURAL NOURISHING<br>AUSTRALIAN SKIN CARE</p>
      <h1 class="product-name">NATIVE<br>HYDRATING<br>SERUM</h1>
      <p class="actives">WITH QUANDONG, LILLI PILLI,<br>KAKADU PLUM</p>
      <p class="claims">100% VEGAN • FOR ALL SKIN TYPES</p>
      <p class="volume">30 ML</p>
    </div>
  </section>

  <section class="label label--back">
    <div class="lace-pattern" role="img" aria-label="Turquoise floral lace pattern on a white honeycomb net"></div>
    <div class="panel panel--info">
      <p class="info-block info-block--narrow">Apply a pearl sized amount between fingertips and warm before gently pressing and smoothing over face, neck and decolletage. Avoid eye area.</p>
      <p class="info-block">Ingredients:<br>Aloe barbadensis (aloe vera) gel*, aloe barbadensis (aloe vera) extract*, citrus glauca (desert lime)*, santalum acuminatum (quandong)*, syzygium leuhmannii (lilli pilli)*, hibiscus sabdariffa (wild rosella)*, terminalia ferdinandiana (kakadu plum)*, backhousia citriodora (lemon myrtle) oil, lavandula angustifolia (australian lavender) oil, citrus aurantium dulcis (australian orange) oil<br>*organic ingredients</p>
      <p class="info-block">Caution: for external use only.<br>Avoid contact with eyes.<br>If irritation occurs,<br>discontinue use.</p>
      <p class="info-block">Made in Australia<br>lorasgrove.com.au</p>
    </div>
  </section>

</main>
</body>
</html>
```